Dental Hygiene referral cards

I am looking to make some referral cards for our hygienists for our dental office. something with our logo and address on the front, and on the back have
hygienist:
__________________
Referred by:
__________________
with a little blurb about what we will give away for a referral.

attached to this is our logo, and a drawing of what im looking for.

I will need this for two of our offices, so just the logo and address will change.

```html
<!DOCTYPE html>
<html lang="en">
<head>
<meta charset="utf-8">
<title>Harbour Ridge Dental – Hygiene Referral Cards</title>
<link href="https://fonts.googleapis.com/css2?family=Cinzel:wght@400;500;600&family=Roboto+Condensed:ital,wght@1,800&display=swap" rel="stylesheet">
<style>
  :root {
    --navy: #17447c;
    --sky: #dbeffb;
    --white: #ffffff;
    --stage: #4c4c4e;
  }
  * { margin: 0; padding: 0; box-sizing: border-box; }
  html, body { width: 1200px; height: 1200px; overflow: hidden; }
  body {
    background: var(--stage);
    position: relative;
    font-family: "Cinzel", "Times New Roman", serif;
    color: var(--navy);
  }
  .card {
    position: absolute;
    width: 562px;
    height: 401px;
    background: var(--white);
    overflow: hidden;
  }
  .card--front { left: 120px; top: 244px; }
  .card--back { left: 498px; top: 684px; }

  /* Front */
  .band {
    position: absolute;
    left: 19px;
    width: 516px;
    height: 33px;
    background: var(--navy);
  }
  .band--top { top: 31px; }
  .band--bottom { top: 335px; }
  .brand {
    position: absolute;
    left: 20px;
    top: 128px;
    width: 230px;
    text-align: center;
  }
  .brand__dot {
    display: block;
    width: 46px;
    height: 46px;
    margin: 0 auto 10px;
    border-radius: 50%;
    background: var(--navy);
  }
  .brand__name {
    font-size: 21px;
    font-weight: 600;
    line-height: 1.15;
    letter-spacing: 0.5px;
  }
  .office-title {
    position: absolute;
    left: 270px;
    width: 262px;
    top: 78px;
    text-align: center;
  }
  .office-title__main { font-size: 24px; font-weight: 500; letter-spacing: 0.5px; line-height: 1.1; }
  .office-title__sub { font-size: 16px; font-weight: 500; letter-spacing: 1px; margin-top: 4px; }
  .appointment {
    position: absolute;
    left: 259px;
    top: 143px;
    width: 276px;
    height: 171px;
    background: var(--sky);
    padding: 44px 0 0 17px;
    font-size: 12px;
    letter-spacing: 0.3px;
  }
  .appointment__row { white-space: nowrap; }
  .appointment__row + .appointment__row { margin-top: 29px; }

  /* Back */
  .back-shapes { position: absolute; inset: 0; }
  .hygienist {
    position: absolute;
    left: 320px;
    width: 230px;
    top: 52px;
    text-align: center;
    color: var(--white);
    font-size: 28px;
    font-weight: 500;
    letter-spacing: 0.5px;
  }
  .referred {
    position: absolute;
    left: 220px;
    top: 190px;
    font-size: 13px;
    letter-spacing: 0.4px;
    white-space: nowrap;
  }
  .blurb {
    position: absolute;
    left: 150px;
    width: 372px;
    top: 238px;
    text-align: center;
    font-size: 20px;
    line-height: 27px;
    letter-spacing: 0.4px;
  }
  .badge-text {
    font-family: "Roboto Condensed", "Arial Narrow", sans-serif;
    font-style: italic;
    font-weight: 800;
  }
</style>
</head>
<body>

<section class="card card--front" aria-label="Card front">
  <div class="band band--top"></div>
  <div class="brand">
    <span class="brand__dot"></span>
    <p class="brand__name">Harbour Ridge<br>Dental</p>
  </div>
  <header class="office-title">
    <p class="office-title__main">HARBOUR RIDGE</p>
    <p class="office-title__sub">DENTAL</p>
  </header>
  <div class="appointment">
    <p class="appointment__row">NAME . . . . . . . . . . . . . . . . . . . . . . . . . . .</p>
    <p class="appointment__row">DATE . . . . . . . . . . . . TIME . . . . . . . . . .</p>
  </div>
  <div class="band band--bottom"></div>
</section>

<section class="card card--back" aria-label="Card back">
  <svg class="back-shapes" width="562" height="401" viewBox="0 0 562 401">
    <rect class="accent-rule" x="0" y="24" width="300" height="13" fill="var(--navy)"/>
    <polygon class="title-panel" points="313,0 562,0 562,118 222,118" fill="var(--navy)"/>
    <polygon class="field-panel" points="210,132 562,132 562,401 0,401" fill="var(--sky)"/>
    <g class="offer-badge">
      <polygon points="36,60 180,60 170,144 28,144" fill="var(--sky)"/>
      <polygon points="70,162 140,162 108,190" fill="var(--navy)"/>
      <polygon points="54,132 162,132 158,162 50,162" fill="var(--navy)"/>
      <polygon points="186,50 196,62 184,64" fill="var(--navy)"/>
      <polygon points="188,70 200,76 190,80" fill="var(--navy)"/>
      <polygon points="12,134 22,140 14,146" fill="var(--navy)"/>
      <polygon points="16,122 24,130 14,128" fill="var(--navy)"/>
      <text class="badge-text" x="106" y="92" text-anchor="middle" font-size="26" fill="var(--navy)">FREE</text>
      <text class="badge-text" x="102" y="122" text-anchor="middle" font-size="26" fill="var(--navy)">BRIGHTWAVE</text>
      <text class="badge-text" x="106" y="153" text-anchor="middle" font-size="18" fill="var(--white)">Tooth brush</text>
    </g>
  </svg>
  <p class="hygienist">HYGENIST :</p>
  <p class="referred">REFERRED BY . . . . . . . . . . . . . . . . . . . . .</p>
  <p class="blurb">REFFER A PAITEBT FOR AN<br>EXAM &amp; A CLEANING &amp; BOTH<br>OF YOU WILL RECIEVE A<br>FREE BRIGHTWAVE TOOTHBRUSH.</p>
</section>

</body>
</html>
```